Our architectural studio needs a new business card

We need a business card design for our studio based in Waterloo in Belgium. We are active in architecture, design and installation.
Our works are contemporary and minimalist. our clients are refined and cultured.
Our business card must be minimalist and refined.

Reason: Some designers have accepted my invitation but they don't have all replied. I want to give them a chance to make one proposal. Paul

Target Market(s)

architecture

Industry/Entity Type

Business

Contact Information for Business Card

studio: paul dorsande studio
paul dorsande, architecte
M. +32 471 982 615
F. +322 618 4097
www.pauldorsande-example.com
paul@pauldorsande-example.com
14 rue des Margelles
1410 Waterloo
Belgium

Font styles to use
Sans Serif

Requirements
Must have
• simple, minimalist, clear, elegant and chic! Black and white
Nice to have
• embossed logo, other format like a square for example
Should not have
• color, fantasy, curves, ...

```html
<!DOCTYPE html>
<html lang="fr">
<head>
<meta charset="utf-8">
<title>Paul Dorsande Studio — Carte de visite</title>
<link rel="stylesheet" href="https://fonts.googleapis.com/css2?family=Lato:wght@300;400;700&display=swap">
<style>
  :root {
    --page-bg: #e9e6e1;
    --card-black: #0c0c0c;
    --card-sheen: #1c1c1c;
    --ink-white: #ffffff;
    --ink-soft: #d9d9d9;
    --rule: #bdbdbd;
  }
  * { box-sizing: border-box; margin: 0; padding: 0; }
  html, body {
    width: 1200px; height: 913px; overflow: hidden;
    background: var(--page-bg);
    font-family: "Lato", Helvetica, Arial, sans-serif;
  }
  .canvas {
    position: relative; width: 1200px; height: 913px;
    display: flex; align-items: center; justify-content: center; gap: 48px;
  }
  .card {
    position: relative; width: 520px; height: 320px;
    border-radius: 22px; overflow: hidden;
    background: linear-gradient(135deg, var(--card-sheen) 0%, var(--card-black) 55%);
    color: var(--ink-white);
    box-shadow: 0 14px 30px rgba(0,0,0,0.25);
  }

  /* Front */
  .card-front {
    display: flex; flex-direction: column; align-items: center; justify-content: center;
  }
  .brand-square {
    width: 64px; height: 64px; background: var(--ink-white); margin-bottom: 30px;
  }
  .brand-name {
    font-size: 15px; font-weight: 700; letter-spacing: 4px; text-transform: uppercase;
  }
  .front-url {
    margin-top: 22px; font-size: 12px; font-weight: 400; letter-spacing: 1.5px; color: var(--ink-soft);
  }

  /* Back */
  .studio-title {
    position: absolute; right: 228px; top: 106px; text-align: right;
  }
  .studio-name {
    font-size: 19px; font-weight: 700; letter-spacing: 0.4px; text-transform: uppercase; white-space: nowrap;
  }
  .studio-role {
    font-size: 17px; font-weight: 300; letter-spacing: 1px; text-transform: uppercase;
  }
  .address {
    position: absolute; right: 228px; bottom: 62px; text-align: right;
    font-size: 12px; font-weight: 300; line-height: 1.5; color: var(--ink-soft);
  }
  .divider {
    position: absolute; left: 306px; top: 128px; width: 1px; height: 76px; background: var(--rule);
  }
  .contacts {
    position: absolute; left: 320px; top: 92px; list-style: none;
    font-size: 10.5px; font-weight: 400; line-height: 1.6; color: var(--ink-soft);
  }
  .contacts li { display: flex; align-items: center; gap: 6px; white-space: nowrap; }
  .contacts svg { width: 10px; height: 10px; flex: none; fill: none; stroke: var(--ink-white); stroke-width: 1.4; }
</style>
</head>
<body>
<main class="canvas">
  <section class="card card-front" aria-label="Recto">
    <div class="brand-square" aria-hidden="true"></div>
    <p class="brand-name">Paul Dorsande Studio</p>
    <p class="front-url">www.pauldorsande-example.com</p>
  </section>

  <section class="card card-back" aria-label="Verso">
    <div class="studio-title">
      <p class="studio-name">Paul Dorsande Studio</p>
      <p class="studio-role">Architecte</p>
    </div>
    <p class="address">14 rue des Margelles 1410<br>Waterloo Belgium</p>
    <div class="divider" aria-hidden="true"></div>
    <ul class="contacts">
      <li><svg viewBox="0 0 10 10"><rect x="2.5" y="0.7" width="5" height="8.6" rx="1"/></svg>+32 471 982 615</li>
      <li><svg viewBox="0 0 10 10"><rect x="1" y="3.5" width="8" height="5"/><rect x="3" y="1" width="4" height="2.5"/></svg>+322 618 4097</li>
      <li><svg viewBox="0 0 10 10"><rect x="0.8" y="2" width="8.4" height="6"/><path d="M0.8 2 L5 5.5 L9.2 2"/></svg>paul@pauldorsande-example.com</li>
      <li><svg viewBox="0 0 10 10"><circle cx="5" cy="5" r="4.2"/><path d="M0.8 5 H9.2 M5 0.8 C2.5 3 2.5 7 5 9.2 M5 0.8 C7.5 3 7.5 7 5 9.2"/></svg>www.pauldorsande-example.com</li>
    </ul>
  </section>
</main>
</body>
</html>
```